Parkinson's Disease Progression

Visually describe the rate of Parkinson progression in the first 15 years following diagnosis. Title: "Patient-Perceived Progression of Parkinsonism"

The attached figure names "meanqol" is the curve that should serve as the basis of this graphic. Everything else-- color, labels, font, etc. describe this curve.
Thank you!

Target Market(s)

People with Parkisnon's Disease, neurologists, family members.

Font styles to use
Sans Serif

Requirements
Must have
• Must have the lines going through these exact numbers
Excellent -- 502
Very good- 661
Good- 895
Fair- 1268
Poor- 1655

LABELS:
Title: "Patient-Perceived Progression of Parkinsonism"
"SWI-TC (Self-Logged Wellbeing Index for Tremor Conditions)" should be the label on the left.
"Quality of Life" should be the label on the right
"Years Since Diagnosis" should be the label on the bottom
Nice to have
• A color scheme that goes from GOOD (low numbers) to BAD (high numbers).

Easy to read (elderly)

```html
<!DOCTYPE html>
<html lang="en">
<head>
<meta charset="utf-8">
<title>Patient-Perceived Progression of Parkinsonism</title>
<link rel="stylesheet" href="https://fonts.googleapis.com/css2?family=EB+Garamond:wght@600;700;800&display=swap">
<style>
  :root {
    --paper: #ffffff;
    --ink: #0a0a0a;
    --panel: #231f20;
    --panel-text: #ffffff;
    --rule: rgba(255,255,255,0.85);
    --grid: rgba(255,255,255,0.45);
  }
  * { margin: 0; padding: 0; box-sizing: border-box; }
  html, body { width: 1200px; height: 974px; overflow: hidden; background: var(--paper); }
  body { font-family: "EB Garamond", Georgia, serif; color: var(--ink); }
  .poster { position: relative; width: 1200px; height: 974px; }

  .title {
    position: absolute; left: 0; top: 42px; width: 1200px;
    padding-left: 12px;
    text-align: center; font-weight: 800; font-size: 76px; line-height: 80px;
    letter-spacing: 0.2px;
  }

  .axis-panel {
    position: absolute; background: var(--panel); color: var(--panel-text);
    display: flex; align-items: center; justify-content: center;
    font-weight: 700;
  }
  .axis-panel--left { left: 69px; top: 245px; width: 89px; height: 513px; }
  .axis-panel--right { left: 1041px; top: 245px; width: 89px; height: 513px; }
  .axis-panel--bottom { left: 311px; top: 822px; width: 575px; height: 89px; font-size: 46px; }
  .vertical-label { transform: rotate(-90deg); white-space: nowrap; font-size: 48px; }

  .chart { position: absolute; left: 311px; top: 245px; width: 575px; height: 513px; }

  .score-tick {
    position: absolute; right: 898px; font-weight: 700; font-size: 23px;
    transform: translateY(-50%); line-height: 1; white-space: nowrap;
  }
  .score-tick::after {
    content: ""; display: inline-block; width: 11px; height: 1.5px;
    background: var(--ink); vertical-align: middle; margin-left: 7px;
  }

  .year-tick {
    position: absolute; top: 781px; width: 60px; margin-left: -30px;
    text-align: center; font-weight: 700; font-size: 23px; line-height: 1;
  }

  .band-label {
    position: absolute; left: 895px; font-weight: 700; font-size: 26px;
    transform: translateY(-50%); line-height: 1; white-space: nowrap;
  }
</style>
</head>
<body>
<main class="poster">
  <h1 class="title">Patient-Perceived<br>Progression of Parkinsonism</h1>

  <div class="axis-panel axis-panel--left"><span class="vertical-label">SWI-TC</span></div>
  <div class="axis-panel axis-panel--right"><span class="vertical-label">Quality of Life</span></div>
  <div class="axis-panel axis-panel--bottom">Years Since Diagnosis</div>

  <svg class="chart" viewBox="0 0 575 513" role="img" aria-label="Mean SWI-TC score rising over 15 years since diagnosis, from Excellent into Fair">
    <defs>
      <linearGradient id="band-top" x1="0" y1="0" x2="0" y2="1"><stop offset="0" stop-color="#3d0508"/><stop offset="1" stop-color="#221516"/></linearGradient>
      <linearGradient id="band-poor" x1="0" y1="0" x2="0" y2="1"><stop offset="0" stop-color="#880910"/><stop offset="1" stop-color="#580005"/></linearGradient>
      <linearGradient id="band-fair" x1="0" y1="0" x2="0" y2="1"><stop offset="0" stop-color="#ba4526"/><stop offset="1" stop-color="#7a2b14"/></linearGradient>
      <linearGradient id="band-good" x1="0" y1="0" x2="0" y2="1"><stop offset="0" stop-color="#c59d08"/><stop offset="1" stop-color="#8a7424"/></linearGradient>
      <linearGradient id="band-verygood" x1="0" y1="0" x2="0" y2="1"><stop offset="0" stop-color="#156c3e"/><stop offset="1" stop-color="#043a1c"/></linearGradient>
      <linearGradient id="band-excellent" x1="0" y1="0" x2="0" y2="1"><stop offset="0" stop-color="#15346a"/><stop offset="1" stop-color="#0d1b47"/></linearGradient>
    </defs>
    <rect x="0" y="0" width="575" height="55" fill="url(#band-top)"/>
    <rect x="0" y="55" width="575" height="111" fill="url(#band-poor)"/>
    <rect x="0" y="166" width="575" height="107" fill="url(#band-fair)"/>
    <rect x="0" y="273" width="575" height="66" fill="url(#band-good)"/>
    <rect x="0" y="339" width="575" height="46" fill="url(#band-verygood)"/>
    <rect x="0" y="385" width="575" height="128" fill="url(#band-excellent)"/>

    <g stroke="var(--rule)" stroke-width="1.2">
      <line x1="0" y1="55" x2="575" y2="55"/>
      <line x1="0" y1="166" x2="575" y2="166"/>
      <line x1="0" y1="273" x2="575" y2="273"/>
      <line x1="0" y1="339" x2="575" y2="339"/>
      <line x1="0" y1="385" x2="575" y2="385"/>
    </g>
    <g stroke="var(--grid)" stroke-width="1" stroke-dasharray="4 4">
      <line x1="26.5" y1="0" x2="26.5" y2="513"/>
      <line x1="200" y1="0" x2="200" y2="513"/>
      <line x1="373" y1="0" x2="373" y2="513"/>
      <line x1="547" y1="0" x2="547" y2="513"/>
    </g>

    <g fill="none" stroke="#fff" stroke-linecap="round">
      <path stroke-width="2.4" stroke-dasharray="3 4"
        d="M26.5 374 C70 366 100 352 130 339 C160 325 180 313 200 311 C230 307 250 311 270 308 C310 302 340 285 373 266 C400 250 420 237 443 227 C465 217 475 206 486 196 C505 190 530 184 547 177"/>
      <path stroke-width="2.4" stroke-dasharray="3 4"
        d="M26.5 433 C50 410 70 395 96 380 C140 356 170 336 200 331 C230 327 250 328 270 323 C310 313 340 298 373 286 C410 272 445 258 477 252 C510 247 530 252 547 257"/>
      <path stroke-width="4"
        d="M26.5 403 C60 386 90 370 113 356 C135 343 150 331 166 323 C180 318 190 316 200 316 C225 314 240 318 252 316 C275 313 290 310 304 305 C330 295 350 283 373 272 C400 259 420 250 443 243 C480 232 515 225 547 217"/>
    </g>
  </svg>

  <div class="score-tick" style="top:300px">1655</div>
  <div class="score-tick" style="top:411px">1268</div>
  <div class="score-tick" style="top:518px">895</div>
  <div class="score-tick" style="top:584px">661</div>
  <div class="score-tick" style="top:630px">502</div>

  <div class="year-tick" style="left:337.5px">0</div>
  <div class="year-tick" style="left:511px">5</div>
  <div class="year-tick" style="left:684px">10</div>
  <div class="year-tick" style="left:858px">15</div>

  <div class="band-label" style="top:328px">Poor</div>
  <div class="band-label" style="top:438px">Fair</div>
  <div class="band-label" style="top:544px">Good</div>
  <div class="band-label" style="top:610px">Very Good</div>
  <div class="band-label" style="top:657px">Excellent</div>
</main>
</body>
</html>
```